The Quietly Broken Map of HOME and ways to endure every season

Not sure.It is about Life injustice and how to face the truth and deal with anything that comes.It touched on Love Identity Finance Emotions

Target Market(s)

18-55

Industry/Entity Type

Life Coaching

Requirements
Must have
• A line through 'Broken'
Nice to have
• An image that captures the interest

```html
<!DOCTYPE html>
<html lang="en">
<head>
<meta charset="utf-8">
<title>The Quietly Broken Map of Home — Book Cover</title>
<link rel="stylesheet" href="https://fonts.googleapis.com/css2?family=Oswald:wght@500;600&family=Mulish:wght@500&family=Pinyon+Script&display=swap">
<style>
  :root {
    --page-bg: #ecebe8;
    --title-orange: #e4501a;
    --title-dark: #4a2310;
    --title-rust: #8b3812;
    --strike-red: #c9261c;
    --script-ink: #2a1d14;
    --subtitle-ink: #4a2a14;
    --author-white: #ffffff;
    --glow: #fff6d2;
    --gold: #f6c034;
    --amber: #eb9a22;
    --ember: #c8581a;
    --earth: #9a3c12;
  }
  * { margin: 0; padding: 0; box-sizing: border-box; }
  html, body {
    width: 1200px;
    height: 762px;
    overflow: hidden;
    background: var(--page-bg);
  }
  .canvas {
    position: relative;
    width: 1200px;
    height: 762px;
    display: flex;
    align-items: center;
    justify-content: center;
  }
  .cover {
    position: relative;
    width: 480px;
    height: 720px;
    overflow: hidden;
  }
  .cover-art {
    position: absolute;
    inset: 0;
    background:
      radial-gradient(ellipse 42% 32% at 34% 74%, var(--glow) 0%, rgba(255,240,180,0.6) 45%, rgba(255,230,150,0) 100%),
      radial-gradient(ellipse 70% 55% at 55% 55%, #fbd650 0%, rgba(246,192,52,0.4) 60%, rgba(246,192,52,0) 100%),
      linear-gradient(180deg, var(--amber) 0%, var(--gold) 30%, var(--gold) 55%, var(--amber) 78%, var(--ember) 92%, var(--earth) 100%);
  }
  .subtitle {
    position: absolute;
    top: 24px;
    left: 0;
    right: 0;
    text-align: center;
    font-family: "Mulish", sans-serif;
    font-weight: 500;
    font-size: 17.5px;
    line-height: 1.35;
    color: var(--subtitle-ink);
  }
  .title-line {
    position: absolute;
    left: 56px;
    font-family: "Oswald", sans-serif;
    font-weight: 600;
    line-height: 1;
    text-transform: uppercase;
    letter-spacing: -0.5px;
  }
  .title-the    { top: 84px;  font-size: 74px; color: var(--title-orange); }
  .title-main   { top: 148px; font-size: 112px; color: var(--title-orange); }
  .title-struck { top: 248px; font-size: 86px; color: var(--title-dark); left: 56px; }
  .title-struck::after {
    content: "";
    position: absolute;
    left: -20px;
    right: -14px;
    top: 48%;
    height: 5px;
    background: var(--strike-red);
    border-radius: 3px;
    transform: rotate(-1.5deg);
  }
  .title-noun   { top: 338px; font-size: 84px; color: var(--title-rust); }
  .title-of     { top: 416px; font-size: 66px; color: var(--title-rust); }
  .title-script {
    position: absolute;
    left: 36px;
    top: 440px;
    font-family: "Pinyon Script", cursive;
    font-size: 170px;
    line-height: 1;
    color: var(--script-ink);
  }
  .theme-word {
    position: absolute;
    font-family: "Mulish", sans-serif;
    font-size: 9px;
    letter-spacing: 1px;
    text-transform: uppercase;
    color: #6a3412;
  }
  .theme-identity { left: 385px; top: 250px; transform: rotate(-78deg); }
  .theme-finance  { left: 330px; top: 340px; transform: rotate(58deg); }
  .theme-love     { left: 418px; top: 340px; transform: rotate(-52deg); }
  .theme-emotions { left: 400px; top: 440px; transform: rotate(-80deg); }
  .author-name {
    position: absolute;
    left: 0;
    right: 0;
    bottom: 26px;
    text-align: center;
    font-family: "Oswald", sans-serif;
    font-weight: 500;
    font-size: 32px;
    letter-spacing: 1.5px;
    color: var(--author-white);
  }
</style>
</head>
<body>
  <main class="canvas">
    <section class="cover">
      <div class="cover-art" role="img" aria-label="Warm painted illustration of a glowing tree with swirling branches in orange and gold"></div>

      <p class="subtitle">How to face the truth about life injustice and<br>deal with anything that comes your way</p>

      <h1 class="book-title">
        <span class="title-line title-the">The</span>
        <span class="title-line title-main">Quietly</span>
        <span class="title-line title-struck">Broken</span>
        <span class="title-line title-noun">Map</span>
        <span class="title-line title-of">Of</span>
        <span class="title-script">Home</span>
      </h1>

      <span class="theme-word theme-identity">Identity</span>
      <span class="theme-word theme-finance">Finance</span>
      <span class="theme-word theme-love">Love</span>
      <span class="theme-word theme-emotions">Emotions</span>

      <p class="author-name">AUTHOR NAME</p>
    </section>
  </main>
</body>
</html>
```